New look while maintaining the Brand identification!

I want a new look for my business card. I want to keep the same colors and feel but change the look and layout a bit. The logo (KINOVALEX Physical therapy Reimagined and the lilypad) must remain the same and in that font.
We are a physical therapy clinic. So we have certification that we can write on the back or services we provide (which is what we currently have on the back of the card as well)

Contact information
2846 Cedar Hollow Rd., #22
Naples, FL 34187
P: (239) 555-0172
F: (239) 555-0198
E: kinovalextherapy@example-mail.com
W: www.kinovalextherapy-example.com

Industry/Entity Type

Physical Therapy

Contact Information for Business Card

Our current cards have the business address and information on the back. But I am willing to have it be in the front.

Font styles to use
Sans Serif

Colors
abd036
fbf289
ec1f27

Requirements
Must have
• Has to be unique!
• Services we provide and/or techniques we do must fit on the card
Nice to have
• Would like to have the front and back somehow linked together. Such that if you set the front next to the back, there is a nice flow of design! Currently the back is white with writing on it.
Should not have
• I like the wave lines as compared to straight lines.

```html
<!DOCTYPE html>
<html lang="en">
<head>
<meta charset="utf-8">
<title>KINOVALEX Business Card</title>
<link href="https://fonts.googleapis.com/css2?family=Arimo:wght@400;700&display=swap" rel="stylesheet">
<style>
  :root {
    --bg: #e9e6e1;
    --card-white: #f7f7f7;
    --card-grey: #e6e6e6;
    --lime: #abd036;
    --lime-light: #cde25a;
    --lime-dark: #96bd1e;
    --olive: #c9bf10;
    --ink: #2b2b2b;
    --white: #ffffff;
  }
  * { margin: 0; padding: 0; box-sizing: border-box; }
  html, body { width: 1200px; height: 1023px; overflow: hidden; }
  body {
    background: var(--bg);
    font-family: "Arimo", Arial, sans-serif;
    position: relative;
  }
  .card {
    position: absolute;
    width: 700px;
    height: 400px;
    border-radius: 18px;
    overflow: hidden;
    box-shadow: 0 4px 14px rgba(0,0,0,0.18);
  }
  /* Front */
  .card-front {
    left: 250px;
    top: 80px;
    background: linear-gradient(135deg, var(--card-white) 0%, var(--card-white) 55%, var(--card-grey) 100%);
  }
  .edge-strip { position: absolute; background: var(--lime); width: 9px; }
  .edge-strip.right-top { right: 0; top: 0; height: 150px; }
  .edge-strip.left-bottom { left: 0; bottom: 0; height: 130px; }
  .person { position: absolute; left: 48px; top: 52px; }
  .person-name {
    color: var(--lime);
    font-size: 32px;
    font-weight: 400;
    letter-spacing: -0.5px;
  }
  .person-credentials {
    color: var(--ink);
    font-size: 14px;
    margin-top: 6px;
  }
  .contact {
    position: absolute;
    left: 48px;
    top: 200px;
    list-style: none;
  }
  .contact li {
    display: flex;
    align-items: center;
    height: 34px;
    font-size: 18px;
    color: var(--ink);
  }
  .contact svg { width: 20px; height: 20px; margin-right: 18px; flex: none; }
  .brand-front {
    position: absolute;
    right: 48px;
    top: 110px;
    display: flex;
    align-items: center;
    gap: 12px;
  }
  .brand-front .brand-dot {
    width: 18px; height: 18px; border-radius: 50%; background: var(--olive);
  }
  .brand-front .brand-name {
    color: var(--olive);
    font-size: 40px;
    font-weight: 700;
    letter-spacing: 1px;
  }
  /* Back */
  .card-back {
    left: 250px;
    top: 543px;
    background: radial-gradient(ellipse at 75% 30%, var(--lime-light) 0%, var(--lime) 50%, var(--lime-dark) 100%);
  }
  .services {
    position: absolute;
    left: 28px;
    right: 28px;
    top: 22px;
    font-size: 14px;
    color: var(--ink);
    white-space: nowrap;
    text-align: center;
  }
  .services .sep { margin: 0 6px; }
  .brand-back {
    position: absolute;
    left: 0; right: 0;
    top: 165px;
    display: flex;
    justify-content: center;
    align-items: center;
    gap: 18px;
  }
  .brand-back .brand-name {
    color: var(--white);
    font-size: 72px;
    font-weight: 700;
    letter-spacing: 2px;
  }
  .brand-back .brand-dot {
    width: 30px; height: 30px; border-radius: 50%; background: var(--white);
  }
</style>
</head>
<body>

<section class="card card-front" aria-label="Business card front">
  <div class="edge-strip right-top"></div>
  <div class="edge-strip left-bottom"></div>

  <div class="person">
    <div class="person-name">Dana Morellis</div>
    <div class="person-credentials">PT, DPT, MSPT, MBA</div>
  </div>

  <ul class="contact">
    <li>
      <svg viewBox="0 0 20 20"><path d="M10 1a6 6 0 0 0-6 6c0 4.5 6 12 6 12s6-7.5 6-12a6 6 0 0 0-6-6z" fill="var(--lime)"/><circle cx="10" cy="7" r="2.3" fill="var(--white)"/></svg>
      2846 Cedar Hollow Rd., #22 Naples, FL 34187
    </li>
    <li>
      <svg viewBox="0 0 20 20"><circle cx="10" cy="10" r="8.5" fill="none" stroke="var(--lime)" stroke-width="1.6"/><path d="M7.5 6c-1 1.5 0 5 3 7 1.2.8 2.3.6 2.8 0l-1.3-1.5-1.2.6c-1-.7-1.8-1.7-2.2-2.8l1-.9L8.8 6z" fill="var(--lime)"/></svg>
      (239) 555-0172
    </li>
    <li>
      <svg viewBox="0 0 20 20"><rect x="5" y="2" width="10" height="6" fill="none" stroke="var(--lime)" stroke-width="1.5"/><rect x="2" y="8" width="16" height="9" rx="1.5" fill="var(--lime)"/><rect x="6" y="11" width="8" height="2" fill="var(--white)"/></svg>
      (239) 555-0198
    </li>
    <li>
      <svg viewBox="0 0 20 20"><rect x="2" y="4.5" width="16" height="11" fill="none" stroke="var(--lime)" stroke-width="1.5"/><path d="M2 4.5l8 6.5 8-6.5" fill="none" stroke="var(--lime)" stroke-width="1.5"/></svg>
      kinovalextherapy@example-mail.com
    </li>
    <li>
      <svg viewBox="0 0 20 20"><g fill="none" stroke="var(--lime)" stroke-width="1.4"><circle cx="10" cy="10" r="8"/><ellipse cx="10" cy="10" rx="3.5" ry="8"/><path d="M2 10h16M3.5 5.5h13M3.5 14.5h13"/></g></svg>
      www.kinovalextherapy-example.com
    </li>
  </ul>

  <div class="brand-front">
    <span class="brand-dot"></span>
    <span class="brand-name">KINOVALEX</span>
  </div>
</section>

<section class="card card-back" aria-label="Business card back">
  <div class="services">
    Neck Pain<span class="sep">|</span>Back Pain<span class="sep">|</span>Hip Pain<span class="sep">|</span>Shoulder Pain<span class="sep">|</span>Vertigo<span class="sep">|</span>Fibromyalgia<span class="sep">|</span>Plantar Fasciitis<span class="sep">|</span>Migraine
  </div>
  <div class="brand-back">
    <span class="brand-name">KINOVALEX</span>
    <span class="brand-dot"></span>
  </div>
</section>

</body>
</html>
```